Travel Consultant Business Card

Hello.. New travel consultant looking seeking a business card that incorporates my new logo. I specialize in cruises but also want to imply land vacation. I am very open to any design and font concepts. I'm looking for a very upbeat modern design that reflects cruise and land vacations. Bright vibrant colors

Target Market(s)

Cruise and Land Vacationers

Industry/Entity Type

Travel Agent

Contact Information for Business Card

I am very open to any design and font concepts. I'm looking for a very upbeat modern design that reflects cruise and land vacations. Bright vibrant colors

Colors

Designer to choose colors to be used in the design.

Requirements
Must have
• Company Name: MapleRidge Journeys---New logo uploaded to be included in design
• My Name: Dolores Kwiatek-Travel Consultant
• Phone Number: (555) 418-7093
• E-Mail Address: mapleridgejourneys@examplemail.net
• Website: www.mapleridgejourneys.example
Nice to have
• My tag line is …..Here to Get You There

```html
<!DOCTYPE html>
<html lang="en">
<head>
<meta charset="utf-8">
<title>MapleRidge Journeys – Business Card</title>
<link rel="stylesheet" href="https://fonts.googleapis.com/css2?family=Montserrat:wght@400;600;800&display=swap">
<style>
  :root {
    --brand-blue: #1560b0;
    --brand-navy: #1a4f98;
    --sky-blue: #2ea3dc;
    --paper: #ffffff;
    --stage: #ececec;
    --rule: #3aa6df;
  }
  * { box-sizing: border-box; margin: 0; padding: 0; }
  html, body { width: 1200px; height: 880px; overflow: hidden; }
  body {
    background: var(--stage);
    font-family: "Montserrat", Arial, sans-serif;
    display: flex;
    flex-direction: column;
    align-items: center;
    justify-content: center;
    gap: 44px;
  }
  .card {
    width: 690px;
    height: 394px;
    border-radius: 26px;
    position: relative;
    overflow: hidden;
    box-shadow: 0 6px 18px rgba(0,0,0,.18);
  }

  /* Front */
  .card-front {
    background: var(--brand-blue);
    color: var(--paper);
    display: flex;
    flex-direction: column;
    align-items: center;
    justify-content: center;
    gap: 22px;
  }
  .brand-name {
    font-weight: 800;
    font-size: 42px;
    letter-spacing: 1px;
    color: var(--paper);
  }
  .front-tagline {
    font-weight: 600;
    font-size: 16px;
    letter-spacing: 5px;
  }

  /* Back */
  .card-back {
    background: var(--paper);
    display: flex;
  }
  .side-band {
    width: 178px;
    background: var(--brand-blue);
    position: relative;
  }
  .side-band .band-name {
    position: absolute;
    left: 50%;
    top: 50%;
    transform: translate(-50%, -50%) rotate(-90deg);
    white-space: nowrap;
    font-weight: 800;
    font-size: 30px;
    color: var(--paper);
  }
  .details {
    flex: 1;
    padding: 78px 40px 0 54px;
  }
  .company {
    font-weight: 800;
    font-size: 29px;
    color: var(--brand-navy);
    text-transform: uppercase;
    letter-spacing: .3px;
  }
  .back-tagline {
    font-weight: 600;
    font-size: 15px;
    letter-spacing: 3.5px;
    color: var(--sky-blue);
    margin-top: 4px;
  }
  .divider {
    border: 0;
    border-top: 1.5px solid var(--rule);
    margin: 10px 0 14px;
    width: 420px;
  }
  .person {
    font-weight: 800;
    font-size: 19px;
    color: var(--brand-navy);
    text-transform: uppercase;
  }
  .role {
    font-size: 15px;
    color: var(--sky-blue);
    margin-top: 1px;
  }
  .contact-list {
    list-style: none;
    margin-top: 20px;
    display: flex;
    flex-direction: column;
    gap: 7px;
  }
  .contact-list li {
    display: flex;
    align-items: center;
    gap: 10px;
    font-size: 15px;
    color: var(--brand-navy);
  }
  .contact-list li.web { color: var(--sky-blue); }
  .contact-icon { width: 24px; height: 24px; flex: none; }
</style>
</head>
<body>

  <section class="card card-front" aria-label="Card front">
    <div class="brand-name">MapleRidge Journeys</div>
    <div class="front-tagline">Here to Get You There</div>
  </section>

  <section class="card card-back" aria-label="Card back">
    <div class="side-band">
      <span class="band-name">MapleRidge Journeys</span>
    </div>
    <div class="details">
      <h1 class="company">MapleRidge Journeys</h1>
      <p class="back-tagline">Here to Get You There</p>
      <hr class="divider">
      <p class="person">Dolores Kwiatek</p>
      <p class="role">Travel Consultant</p>
      <ul class="contact-list">
        <li>
          <svg class="contact-icon" viewBox="0 0 24 24" aria-hidden="true">
            <circle cx="12" cy="12" r="11" fill="none" stroke="#2ea3dc" stroke-width="1.5"/>
            <rect x="8.5" y="6" width="7" height="12" rx="1.2" fill="none" stroke="#1a4f98" stroke-width="1.5"/>
            <circle cx="12" cy="15.6" r=".8" fill="#1a4f98"/>
          </svg>
          (555) 418-7093
        </li>
        <li>
          <svg class="contact-icon" viewBox="0 0 24 24" aria-hidden="true">
            <circle cx="12" cy="12" r="11" fill="none" stroke="#2ea3dc" stroke-width="1.5"/>
            <rect x="6.5" y="8" width="11" height="8" rx="1" fill="#1a4f98"/>
            <path d="M6.8 8.4 L12 12.6 L17.2 8.4" fill="none" stroke="#fff" stroke-width="1.2"/>
          </svg>
          mapleridgejourneys@examplemail.net
        </li>
        <li class="web">
          <svg class="contact-icon" viewBox="0 0 24 24" aria-hidden="true">
            <circle cx="12" cy="12" r="11" fill="none" stroke="#2ea3dc" stroke-width="1.5"/>
            <circle cx="12" cy="12" r="6" fill="none" stroke="#1a4f98" stroke-width="1.3"/>
            <ellipse cx="12" cy="12" rx="2.6" ry="6" fill="none" stroke="#1a4f98" stroke-width="1.1"/>
            <line x1="6" y1="12" x2="18" y2="12" stroke="#1a4f98" stroke-width="1.1"/>
          </svg>
          www.mapleridgejourneys.example
        </li>
      </ul>
    </div>
  </section>

</body>
</html>
```